Sheriff Candidate needs a large yard sign

A candidate for Sheriff needs to have a sign to put in front of businesses and houses that advertise her candidacy.

Target Market(s)

Democrats, voters

Industry/Entity Type

Political

Font styles to use
Sans Serif

Colors
34a7d7
3276b5

Requirements
Must have
• Must have her picture
• Must have the words "Elect Dana Whitlock" - I'd like the name Dana to be smaller Whitlock. "Elect" and "Whitlock" should be the focus.
• at the bottom in a box "Paid for by the Committee to Elect Dana Whitlock"
Nice to have
• it would be good to have her logo as well.
• blue color for democrats and on a white background
Should not have
• pink color

```html
<!DOCTYPE html>
<html lang="en">
<head>
<meta charset="utf-8">
<title>Elect Dana Whitlock for Sheriff</title>
<link href="https://fonts.googleapis.com/css2?family=Bebas+Neue&family=Oswald:wght@500;700&display=swap" rel="stylesheet">
<style>
  :root {
    --navy: #2b3990;
    --title-blue: #2e3d96;
    --red: #c1272d;
    --white: #ffffff;
    --photo-dark: #5c5c5e;
    --photo-light: #a3a3a5;
    --badge-gold: #c99a2e;
    --badge-deep: #8a6414;
  }
  * { margin: 0; padding: 0; box-sizing: border-box; }
  html, body { width: 849px; height: 1200px; overflow: hidden; background: var(--white); }
  .yard-sign { position: relative; width: 849px; height: 1200px; background: var(--white); overflow: hidden; }
  .ribbon { position: absolute; top: 563px; height: 38px; background: var(--red); }
  .ribbon--left { left: 0; width: 164px; }
  .ribbon--right { left: 679px; width: 170px; }
  .blue-field { position: absolute; left: 0; top: 601px; width: 849px; height: 599px; background: var(--navy); }
  .headline, .ornaments { position: absolute; left: 0; top: 0; width: 849px; height: 1200px; }
  .headline text.elect { font-family: "Bebas Neue", sans-serif; fill: var(--title-blue); }
  .headline text.surname { font-family: "Bebas Neue", sans-serif; fill: var(--white); }
  .candidate-photo {
    position: absolute; left: 164px; top: 209px; width: 515px; height: 661px;
    background: radial-gradient(ellipse at 55% 40%, var(--photo-light), var(--photo-dark) 85%);
  }
  .tagline {
    position: absolute; left: 165px; top: 888px;
    font-family: "Oswald", sans-serif; font-weight: 500; font-size: 44px; letter-spacing: 2px;
    color: var(--white); line-height: 1;
  }
  .campaign-badge {
    position: absolute; left: 555px; top: 669px; width: 262px; height: 262px; border-radius: 50%;
    background: radial-gradient(circle at 40% 35%, var(--badge-gold), var(--badge-deep));
    display: flex; align-items: center; justify-content: center; text-align: center;
  }
  .campaign-badge span {
    font-family: "Oswald", sans-serif; font-weight: 700; font-size: 30px; line-height: 1.1;
    color: var(--white); letter-spacing: 1px;
  }
  .disclaimer {
    position: absolute; left: 0; width: 849px; top: 1150px; text-align: center;
    font-family: "Oswald", sans-serif; font-weight: 700; font-size: 17px; letter-spacing: 1px;
    color: var(--white); text-transform: uppercase;
  }
</style>
</head>
<body>
<main class="yard-sign">
  <div class="ribbon ribbon--left"></div>
  <div class="ribbon ribbon--right"></div>
  <div class="blue-field"></div>

  <svg class="ornaments" viewBox="0 0 849 1200" aria-hidden="true">
    <defs>
      <polygon id="star" points="0,-1 0.235,-0.324 0.951,-0.309 0.38,0.124 0.588,0.809 0,0.4 -0.588,0.809 -0.38,0.124 -0.951,-0.309 -0.235,-0.324"/>
    </defs>
    <g fill="var(--title-blue)">
      <use href="#star" transform="translate(96 111) scale(20)"/>
      <use href="#star" transform="translate(755 111) scale(20)"/>
    </g>
    <g fill="var(--white)">
      <use href="#star" transform="translate(22 583) scale(11)"/>
      <use href="#star" transform="translate(70 583) scale(11)"/>
      <use href="#star" transform="translate(130 583) scale(11)"/>
      <use href="#star" transform="translate(708 583) scale(11)"/>
      <use href="#star" transform="translate(754 583) scale(11)"/>
      <use href="#star" transform="translate(817 583) scale(11)"/>
    </g>
  </svg>

  <div class="candidate-photo" role="img" aria-label="Portrait photograph of candidate Dana Whitlock"></div>

  <svg class="headline" viewBox="0 0 849 1200">
    <text class="elect" x="198" y="177" font-size="232" textLength="455" lengthAdjust="spacingAndGlyphs">ELECT</text>
    <text class="surname" x="28" y="1133" font-size="244" textLength="792" lengthAdjust="spacingAndGlyphs">WHITLOCK</text>
  </svg>

  <div class="campaign-badge"><span>WHITLOCK<br>FOR SHERIFF</span></div>

  <p class="tagline">DANA FOR SHERIFF</p>
  <p class="disclaimer">Paid for by the Committee to Elect Dana Whitlock</p>
</main>
</body>
</html>
```